DOVR Business Card Design Project

Company Name: DOVR (Dove Operational Versatile Resources) JLT.
Office Address: Office No 218, Saffron Crest Tower, Palmera Bay Towers, Dubai, U.A.E
Company line of business:
1) Currently we have a POS solution for retail outlets like duty free shops, supermarkets, department stores etc... The solution is deployed in Harbor Gate Retail on 350 POS and in Coralline Port Retail on 100 POS. So our main line of business is the deployment of this solution in retail outlets locally or regionally. We have already deployed the solution in India and Australia.
2) Integration of other third party POS systems with an online credit authorization netwotk in the UAE. This will enable POS applications to connect directly to the acquiring banks without needing an EFT terminal like Paxoline or Tramodex. The credit card payment is completed at the POS.
3) Other solutions that are targeting retail outlets like mobile POS, queue busting solutions, stock taking solutions using hand held devices, transaction capture systems, etc...
4) Other IT services like support of call center solutions from Bramwell Systems and development of new solutions as per customer requirements.
We need a business card design for the company. We don't have any specific requirements and will eave up to the designers to come up with creative designs. At the moment we still don't have a letter head design and the only thing that we have is the company logo that we will upload shortly.
Updates
Dear All,
I just uploaded the logo source files. I am sorry for the delay.
Regards
Tarek Demirci
I would like the business cards to have the following details:
Company Tel No
Company Fax No
Company Website Address
Employee Name
Employee Title
Employee Mobile Number
Employee Email Address

```html
<!DOCTYPE html>
<html lang="en">
<head>
<meta charset="utf-8">
<title>DOVR Business Card</title>
<link rel="stylesheet" href="https://fonts.googleapis.com/css2?family=Marcellus&family=Marcellus+SC&display=swap">
<style>
  :root {
    --page: #ffffff;
    --card: #ffffff;
    --card-edge: #8c9ea3;
    --card-edge-low: #d9a6b8;
    --band: #dde4e3;
    --lime-core: #e9ff7a;
    --lime: #c9f200;
    --lime-edge: #b8e400;
    --panel-border: #a9b0a8;
    --ink: #1c1f1c;
    --mark: #1e88d8;
  }
  * { box-sizing: border-box; margin: 0; padding: 0; }
  html, body {
    width: 1200px;
    height: 389px;
    overflow: hidden;
    background: var(--page);
  }
  .sheet {
    position: relative;
    width: 1200px;
    height: 389px;
  }
  .card {
    position: absolute;
    top: 2px;
    width: 588px;
    height: 384px;
    background: var(--card);
    border: 1px solid var(--card-edge);
    border-bottom-color: var(--card-edge-low);
    overflow: hidden;
  }
  .card--front { left: 2px; }
  .card--back { left: 610px; }

  .band {
    position: absolute;
    top: 0;
    left: 315px;
    width: 221px;
    height: 100%;
    background: var(--band);
    box-shadow: inset 0 0 10px rgba(255,255,255,0.8);
  }

  .brand {
    position: absolute;
    display: flex;
    align-items: center;
    font-family: "Marcellus", serif;
    color: var(--ink);
  }
  .brand__dot {
    border-radius: 50%;
    background: var(--mark);
    flex: none;
  }
  .brand--small {
    left: 64px;
    top: 162px;
    gap: 14px;
  }
  .brand--small .brand__dot { width: 48px; height: 48px; }
  .brand--small .brand__name { font-size: 44px; letter-spacing: 1px; line-height: 1; }

  .brand--large {
    left: 0;
    right: 0;
    top: 0;
    bottom: 0;
    justify-content: center;
    gap: 30px;
  }
  .brand--large .brand__dot { width: 110px; height: 110px; }
  .brand--large .brand__name { font-size: 100px; letter-spacing: 3px; line-height: 1; }

  .contact-panel {
    position: absolute;
    left: 294px;
    top: 80px;
    width: 264px;
    height: 228px;
    border: 1px solid var(--panel-border);
    background: radial-gradient(ellipse at 55% 60%, var(--lime-core) 0%, var(--lime) 60%, var(--lime-edge) 100%);
    color: var(--ink);
    font-family: "Marcellus", serif;
  }
  .contact-panel__name {
    margin-top: 20px;
    text-align: center;
    font-size: 26px;
    line-height: 1;
  }
  .contact-panel__title {
    margin-top: 4px;
    text-align: center;
    font-family: "Marcellus SC", serif;
    font-size: 19px;
    letter-spacing: 0.5px;
    line-height: 1.1;
  }
  .contact-panel__list {
    list-style: none;
    padding-left: 33px;
    font-size: 16px;
    line-height: 21px;
  }
  .contact-panel__list--personal { margin-top: 16px; }
  .contact-panel__list--company { margin-top: 21px; }
</style>
</head>
<body>
<main class="sheet">
  <section class="card card--front" aria-label="Business card front">
    <div class="band"></div>
    <div class="brand brand--small">
      <span class="brand__dot"></span>
      <span class="brand__name">DOVR</span>
    </div>
    <div class="contact-panel">
      <p class="contact-panel__name">Employee Name</p>
      <p class="contact-panel__title">Employee Title</p>
      <ul class="contact-panel__list contact-panel__list--personal">
        <li>Employee mobile No</li>
        <li>Employee email address</li>
      </ul>
      <ul class="contact-panel__list contact-panel__list--company">
        <li>Company Tel No</li>
        <li>Company Fax No</li>
        <li>Company Website Address</li>
      </ul>
    </div>
  </section>

  <section class="card card--back" aria-label="Business card back">
    <div class="brand brand--large">
      <span class="brand__dot"></span>
      <span class="brand__name">DOVR</span>
    </div>
  </section>
</main>
</body>
</html>
```